Craft oriented film company needs a Business Card design

Hi all,
We're a 2-man band film company in New Zealand called Kestrel Pictures. We're good honest blokes, who are very passionate about the craft of film making. I've attached our current logo which has a bit of a crafty/artisan feel that we like. Feel free to use it - or throw the baby out with the bathwater and start again..... you never know, you might inspire a complete brand re-work.

In any case, the vibe we want to give out is that we are solid, dependable and no bullshit - but without compromising creative excellence and being in the now. We like the 'Brooklyn' artisan style of work.

Preferably single sided.

We need the standard stuff:
Name, job title, cellphone, email address and physical address (this can be smaller if you like - street, suburb, city & zip, country [if you want])

Check out our website to learn more about us: kestrelpictures.example

Target Market(s)

Brand marketers and advertising agency creatives looking for video production.

Industry/Entity Type

Baby

Requirements
Should not have
• Nothing flashy or too 'futuristic', we want it to feel grounded and real. A limited colour palette is preferred.
We don't want any film reels or cameras or anything obvious like that.

```html
<!DOCTYPE html>
<html lang="en">
<head>
<meta charset="utf-8">
<title>Kestrel Pictures – Business Card</title>
<link rel="stylesheet" href="https://fonts.googleapis.com/css2?family=Open+Sans:wght@400;700;800&display=swap">
<style>
  :root {
    --backdrop: #e9e6e1;
    --card-white: #f7f7f7;
    --band-black: #0d0d0d;
    --band-edge: #a9c3c8;
    --ink-light: #ffffff;
    --ink-muted: #9a9a9a;
  }
  html, body {
    margin: 0;
    width: 1200px;
    height: 1023px;
    overflow: hidden;
    background: var(--backdrop);
    font-family: "Open Sans", Arial, sans-serif;
  }
  .card {
    position: absolute;
    left: 180px;
    top: 271px;
    width: 840px;
    height: 480px;
    background: var(--card-white);
    box-shadow: 0 10px 30px rgba(0,0,0,0.18);
    overflow: hidden;
  }
  .card-art {
    position: absolute;
    inset: 0;
  }
  .brand {
    position: absolute;
    left: 330px;
    top: 66px;
    width: 190px;
    height: 190px;
    border-radius: 50%;
    background: var(--band-black);
    display: flex;
    align-items: center;
    justify-content: center;
    text-align: center;
  }
  .brand-name {
    color: var(--ink-light);
    font-weight: 800;
    font-size: 25px;
    line-height: 1.15;
    letter-spacing: 1px;
    text-transform: uppercase;
  }
  .contact {
    position: absolute;
    right: 36px;
    top: 200px;
    list-style: none;
    margin: 0;
    padding: 0;
    color: var(--ink-light);
    font-size: 16px;
    line-height: 28px;
    text-align: right;
  }
  .contact li {
    display: flex;
    align-items: center;
    justify-content: flex-end;
    gap: 10px;
  }
  .contact svg {
    width: 16px;
    height: 16px;
    fill: none;
    stroke: var(--ink-light);
    stroke-width: 1.6;
  }
  .person {
    position: absolute;
    left: 40px;
    top: 318px;
    color: var(--ink-muted);
  }
  .person-name {
    margin: 0;
    font-size: 22px;
    font-weight: 400;
    text-transform: uppercase;
    letter-spacing: 0.5px;
  }
  .person-title {
    margin: 2px 0 16px;
    font-size: 14px;
  }
  .person-address {
    font-style: normal;
    font-size: 16px;
    line-height: 24px;
    color: #b8b8b8;
  }
</style>
</head>
<body>
  <div class="card">
    <svg class="card-art" viewBox="0 0 840 480" aria-hidden="true">
      <path d="M0,262 C260,300 520,200 840,150 L840,332 C600,362 300,420 120,480 L0,480 Z"
            fill="var(--band-edge)"/>
      <path d="M0,272 C260,310 520,210 840,160 L840,322 C600,352 300,410 100,480 L0,480 Z"
            fill="var(--band-black)"/>
    </svg>

    <div class="brand">
      <span class="brand-name">Kestrel<br>Pictures</span>
    </div>

    <ul class="contact">
      <li>+64-21-55-0147
        <svg viewBox="0 0 16 16"><rect x="4" y="1.5" width="8" height="13" rx="1.5"/><line x1="7" y1="12" x2="9" y2="12"/></svg>
      </li>
      <li>info@kestrelpictures.example
        <svg viewBox="0 0 16 16"><rect x="1.5" y="3.5" width="13" height="9"/><polyline points="1.5,3.5 8,9 14.5,3.5"/></svg>
      </li>
      <li>www.kestrelpictures.example
        <svg viewBox="0 0 16 16"><circle cx="8" cy="8" r="6.5"/><ellipse cx="8" cy="8" rx="3" ry="6.5"/><line x1="1.5" y1="8" x2="14.5" y2="8"/></svg>
      </li>
    </ul>

    <div class="person">
      <h1 class="person-name">Rowan Hale</h1>
      <p class="person-title">Director</p>
      <address class="person-address">48 Harbour Lane, Unit 3<br>Ponsonby, Auckland 1011</address>
    </div>
  </div>
</body>
</html>
```